New Flyer Design Project for a KBTW Business

I have started an KBTW business and want to create a Flyer and Brochure.
We already have a webpage and logo.
Below link is a reference point
https://www.plimvarto.com.au/design/71834620
webpage is www.belvorcare.com.au
Please match the colour from the webpage and the colour from KBTW webpage.
I also like the tri-folded brochure.
I want pictures associated with the disability sector.
Please use
contact number to be (02) 7341 9256
Email : Enquire@belvorcare.com.au
Thank you.
Disability sector
Disability

```html
<!DOCTYPE html>
<html lang="en">
<head>
<meta charset="utf-8">
<title>Belvor Care – Brochure and Flyer</title>
<link href="https://fonts.googleapis.com/css2?family=Montserrat:wght@400;500;600;700;800&display=swap" rel="stylesheet">
<style>
:root{
  --board:#a7a8ac;
  --paper:#ffffff;
  --navy:#0f3a48;
  --teal:#49b5b5;
  --ink:#1f2a30;
  --body:#4a555b;
  --rule:#e6eaec;
}
*{box-sizing:border-box;margin:0;padding:0}
html,body{width:844px;height:1200px;overflow:hidden;background:var(--board);font-family:"Montserrat",sans-serif;color:var(--ink)}
.board{position:relative;width:844px;height:1200px}
.sheet{position:absolute;background:var(--paper);overflow:hidden}
.sheet>svg{position:absolute;left:0;top:0}
.brochure{left:216px;width:423px;height:299px}
.brochure.outside{top:59px}
.brochure.inside{top:369px}
.fold{position:absolute;top:0;bottom:0;width:1px;background:var(--rule)}
.abs{position:absolute}
.logo{display:flex;align-items:center;gap:4px;font-weight:700;color:var(--navy);font-size:7.5px;line-height:1}
.logo .dot{width:10px;height:10px;border-radius:50%;background:var(--teal)}
.headline{font-weight:800;color:var(--navy);line-height:.95;letter-spacing:-.2px}
.sub{color:var(--teal);font-weight:500}
.tagline{font-weight:500;color:var(--ink);line-height:1.35}
.copy{color:var(--body);font-size:4.3px;line-height:1.6;text-align:justify}
.copy p+p{margin-top:5px}
.copy h4{font-size:5.2px;color:var(--navy);font-weight:700;margin:7px 0 2px}
.why{color:var(--teal);font-weight:800;line-height:1}
.contact{position:absolute;border-radius:6px;color:#fff;font-weight:700;display:flex;flex-direction:column;justify-content:center;gap:4px;padding-left:11px}
.contact.dark{background:var(--navy)}
.contact.light{background:var(--teal)}
.contact .row{display:flex;align-items:center;gap:5px}
.contact svg{flex:none}
.feature{position:absolute;left:308px;width:96px}
.feature h5{font-size:5px;color:var(--teal);font-weight:700;margin-bottom:2px}
.feature p{font-size:4px;color:#d8e8ea;line-height:1.55}
.icon-bubble{position:absolute;width:12px;height:12px;border-radius:50%;background:var(--teal)}
.label{position:absolute;border:1.5px solid var(--ink);border-radius:10px;font-weight:800;font-size:13px;display:flex;align-items:center;justify-content:center;color:var(--ink)}
.badge{position:absolute;border:1px solid #fff;border-radius:6px;display:flex;flex-direction:column;align-items:center;justify-content:center;font-weight:800;font-size:11px;line-height:1;background:rgba(255,255,255,.15)}
.badge span:first-child{color:var(--navy)}
.badge span:last-child{color:#fff}
</style>
</head>
<body>
<div class="board">

  <!-- Brochure outside -->
  <section class="sheet brochure outside">
    <svg width="423" height="299" viewBox="0 0 423 299">
      <defs>
        <linearGradient id="grayTone" x1="0" x2="1" y1="0" y2="1"><stop offset="0" stop-color="#f2f2f2"/><stop offset="1" stop-color="#a5a5a5"/></linearGradient>
        <linearGradient id="warmTone" x1="0" x2="1" y1="0" y2="1"><stop offset="0" stop-color="#ead9a6"/><stop offset="1" stop-color="#c9714f"/></linearGradient>
      </defs>
      <path d="M0,150 C40,140 70,142 100,160" fill="none" stroke="var(--rule)" stroke-width="8"/>
      <path d="M0,162 C35,150 70,150 100,175" fill="none" stroke="var(--navy)" stroke-width="2"/>
      <path d="M175,218 C250,205 300,120 423,100 L423,260 C350,250 300,245 250,250 Z" fill="var(--navy)"/>
      <path d="M0,245 C60,225 130,205 200,212 C270,220 330,250 423,255 L423,299 L0,299 Z" fill="var(--teal)"/>
      <path d="M282,75 C320,55 370,42 423,36 L423,103 C370,112 320,128 282,148 Z" fill="url(#grayTone)" role="img" aria-label="Photo area: young woman writing at a desk, in grey tones"/>
      <rect x="8" y="138" width="168" height="161" rx="4" fill="url(#warmTone)" role="img" aria-label="Photo area: two smiling people, a man in a yellow shirt and a woman in a red jumper"/>
    </svg>
    <div class="fold" style="left:141px"></div>
    <div class="fold" style="left:282px"></div>

    <div class="abs logo" style="left:21px;top:24px"><span class="dot"></span>Belvor Care</div>
    <h1 class="abs headline" style="left:21px;top:57px;font-size:19px">Disability<br>Support</h1>
    <div class="abs sub" style="left:21px;top:98px;font-size:11px">Provider</div>
    <div class="abs tagline" style="left:21px;top:120px;font-size:5.6px">At Belvor Care,<br>we're life enhancers!</div>

    <div class="abs why" style="left:151px;top:29px;font-size:22px">Why</div>
    <div class="abs" style="left:151px;top:54px;font-size:7.5px;font-weight:700">Choose Belvor Care?</div>
    <div class="abs copy" style="left:151px;top:77px;width:117px">Belvor Care was born out of a desire to make a real and lasting difference in the lives of our participants and the wider community. We approach each individual with empathy, respect, and a deep commitment to understanding their unique story, needs, and aspirations.</div>

    <div class="contact dark" style="left:153px;top:240px;width:111px;height:48px;font-size:5.6px">
      <div class="row"><svg width="7" height="7" viewBox="0 0 10 10"><path d="M2,1 L4,1 L5,3 L4,4 C4.5,5.5 5.5,6.5 7,7 L8,6 L9,7 L9,9 C5,9 1,5 2,1Z" fill="none" stroke="#fff" stroke-width=".8"/></svg>(02) 7341 9256</div>
      <div class="row" style="font-size:4.6px"><svg width="7" height="7" viewBox="0 0 10 10"><rect x="1" y="2.5" width="8" height="5.5" fill="none" stroke="#fff" stroke-width=".8"/><path d="M1,2.5 L5,6 L9,2.5" fill="none" stroke="#fff" stroke-width=".8"/></svg>Enquire@belvorcare.com.au</div>
      <div class="row" style="font-size:4.6px"><svg width="7" height="7" viewBox="0 0 10 10"><circle cx="5" cy="5" r="4" fill="none" stroke="#fff" stroke-width=".8"/><path d="M1,5 H9 M5,1 C2.5,3.5 2.5,6.5 5,9 M5,1 C7.5,3.5 7.5,6.5 5,9" fill="none" stroke="#fff" stroke-width=".6"/></svg>belvorcare.com.au</div>
    </div>

    <div class="abs" style="left:299px;top:24px;font-size:10px;font-weight:700;color:var(--teal)">Empowering</div>
    <div class="abs" style="left:299px;top:36px;font-size:5.3px;font-weight:700;color:var(--navy)">Lives in NSW</div>

    <span class="icon-bubble" style="left:346px;top:126px"></span>
    <div class="feature" style="top:149px"><h5>People &amp; Family Oriented</h5><p>We see each participant as part of our extended family, ensuring a warm, personal touch in everything we do.</p></div>
    <span class="icon-bubble" style="left:346px;top:189px"></span>
    <div class="feature" style="top:207px"><h5>Enriching Lives</h5><p>Every day, we're fuelled by our mission to make a tangible difference in the community.</p></div>
    <span class="icon-bubble" style="left:348px;top:241px;width:8px;height:8px"></span>
    <div class="feature" style="top:258px"><h5 style="color:var(--navy)">Fun &amp; Fulfilment</h5><p style="color:#eefafa">We believe in adding a dash of fun to our services because a joyful journey is as important as the destination.</p></div>
  </section>

  <!-- Brochure inside -->
  <section class="sheet brochure inside">
    <svg width="423" height="299" viewBox="0 0 423 299">
      <defs>
        <linearGradient id="grayFade" x1="0" x2="1"><stop offset="0" stop-color="#9a9c9d"/><stop offset=".6" stop-color="#cfcfcf"/><stop offset="1" stop-color="#ffffff"/></linearGradient>
        <linearGradient id="rustTone" x1="0" x2="1" y1="0" y2="1"><stop offset="0" stop-color="#dcc3b5"/><stop offset="1" stop-color="#bf5a36"/></linearGradient>
      </defs>
      <path d="M305,0 C340,25 380,40 423,45 L423,0 Z" fill="var(--navy)"/>
      <path d="M0,210 C60,190 120,170 190,170 C230,170 260,175 282,180 L282,299 L0,299 Z" fill="url(#grayFade)" role="img" aria-label="Photo area: smiling man using a wheelchair in a library, in grey tones"/>
      <path d="M0,210 C40,200 70,200 100,200 L130,299 L0,299 Z" fill="var(--navy)"/>
      <path d="M110,235 L210,299 L120,299 Z" fill="var(--teal)"/>
      <rect x="8" y="138" width="116" height="161" rx="4" fill="url(#rustTone)" role="img" aria-label="Photo area: woman with curly hair in a red jumper, arms folded"/>
    </svg>
    <div class="fold" style="left:141px"></div>
    <div class="fold" style="left:282px"></div>

    <div class="abs logo" style="left:21px;top:24px"><span class="dot"></span>Belvor Care</div>
    <h1 class="abs headline" style="left:21px;top:57px;font-size:19px">Disability<br>Support</h1>
    <div class="abs sub" style="left:21px;top:98px;font-size:11px">Provider</div>
    <div class="abs tagline" style="left:21px;top:120px;font-size:5.6px">At Belvor Care,<br>we're life enhancers!</div>

    <h2 class="abs headline" style="left:151px;top:23px;font-size:15px">Beyond the<br>Essentials</h2>
    <div class="abs copy" style="left:151px;top:62px;width:117px">
      <p>At Belvor Care, we understand that supporting our participants means going beyond the essentials. It's about enriching your life with activities and experiences that bring joy, excitement, and a sense of accomplishment.</p>
      <p>From leisure activities to skill-building workshops, our lifestyle enhancement programs are designed to add a touch of fun, creativity, and adventure to your daily life, ensuring that every day is an opportunity to experience something new and delightful.</p>
    </div>

    <div class="contact light" style="left:153px;top:221px;width:111px;height:48px;font-size:5.6px">
      <div class="row"><svg width="7" height="7" viewBox="0 0 10 10"><path d="M2,1 L4,1 L5,3 L4,4 C4.5,5.5 5.5,6.5 7,7 L8,6 L9,7 L9,9 C5,9 1,5 2,1Z" fill="none" stroke="#fff" stroke-width=".8"/></svg>(02) 7341 9256</div>
      <div class="row" style="font-size:4.6px"><svg width="7" height="7" viewBox="0 0 10 10"><rect x="1" y="2.5" width="8" height="5.5" fill="none" stroke="#fff" stroke-width=".8"/><path d="M1,2.5 L5,6 L9,2.5" fill="none" stroke="#fff" stroke-width=".8"/></svg>Enquire@belvorcare.com.au</div>
      <div class="row" style="font-size:4.6px"><svg width="7" height="7" viewBox="0 0 10 10"><circle cx="5" cy="5" r="4" fill="none" stroke="#fff" stroke-width=".8"/><path d="M1,5 H9 M5,1 C2.5,3.5 2.5,6.5 5,9 M5,1 C7.5,3.5 7.5,6.5 5,9" fill="none" stroke="#fff" stroke-width=".6"/></svg>belvorcare.com.au</div>
    </div>

    <h2 class="abs why" style="left:290px;top:43px;width:125px;text-align:center;font-size:16px;line-height:.98">Ways We<br>Deliver Care</h2>
    <div class="abs copy" style="left:294px;top:84px;width:112px">
      <p>Our services are as diverse as the individuals we support. From providing daily living assistance to fostering personal development and skill enhancement, we take pride in our ability to adapt and tailor our services to fit the unique needs and aspirations of each participant.</p>
      <h4>Upskill and gain independence</h4>
      <p style="margin-top:0">Our tailored approach helps you develop essential life skills, from managing daily tasks to learning new talents. With our supportive guidance, you'll not only gain practical abilities but also a sense of self-reliance and achievement.</p>
      <h4>Receive care in your own home</h4>
      <p style="margin-top:0">Our dedicated team provides personalised support tailored to your needs, ensuring you feel safe, supported, and empowered, all within the comfort of your own living space. It's not just care; it's about enhancing your life at home.</p>
      <h4>Get out and about in your community</h4>
      <p style="margin-top:0">Our services focus on helping you engage with the world around you. From social events to community projects, we support you in building connections, experiencing new activities, and enjoying the richness of community life.</p>
    </div>
  </section>

  <div class="label" style="left:353px;top:673px;width:148px;height:21px">Brochure Tri Fold</div>

  <!-- Flyer -->
  <section class="sheet flyer" style="left:291px;top:719px;width:272px;height:385px">
    <svg width="272" height="385" viewBox="0 0 272 385">
      <defs>
        <linearGradient id="grayFade2" x1="0" x2="1"><stop offset="0" stop-color="#9a9c9d"/><stop offset=".6" stop-color="#cacccc"/><stop offset="1" stop-color="#f4f4f4"/></linearGradient>
        <linearGradient id="rustTone2" x1="0" x2="1" y1="0" y2="1"><stop offset="0" stop-color="#dcc3b5"/><stop offset="1" stop-color="#bf5a36"/></linearGradient>
      </defs>
      <path d="M0,240 C40,225 80,225 120,225 C170,220 220,215 272,225 L272,385 L0,385 Z" fill="url(#grayFade2)" role="img" aria-label="Photo area: smiling man using a wheelchair, in grey tones"/>
      <path d="M0,240 C30,232 55,230 80,232 L0,300 Z" fill="var(--teal)"/>
      <path d="M140,330 L272,360 L272,385 L160,385 Z" fill="var(--teal)"/>
      <rect x="0" y="138" width="148" height="247" fill="url(#rustTone2)" role="img" aria-label="Photo area: woman with curly hair in a red jumper, arms folded"/>
    </svg>

    <div class="abs logo" style="left:24px;top:18px;font-size:9px"><span class="dot" style="width:12px;height:12px"></span>Belvor Care</div>
    <h1 class="abs headline" style="left:24px;top:50px;font-size:25px">Disability<br>Support</h1>
    <div class="abs sub" style="left:24px;top:105px;font-size:13px">Provider</div>
    <div class="abs tagline" style="left:157px;top:77px;font-size:7.4px">At Belvor Care,<br>we're life enhancers!</div>

    <div class="abs why" style="left:154px;top:120px;font-size:16px">Why</div>
    <div class="abs" style="left:154px;top:140px;font-size:5.5px;font-weight:700">Choose Belvor Care?</div>
    <div class="abs copy" style="left:154px;top:153px;width:106px">Belvor Care was born out of a desire to make a real and lasting difference in the lives of our participants and the wider community. We approach each individual with empathy, respect, and a deep commitment to understanding their unique story, needs, and aspirations.</div>

    <div class="badge" style="left:150px;top:246px;width:100px;height:35px"><span>Empowering</span><span>Lives in NSW</span></div>

    <div class="contact dark" style="left:145px;top:312px;width:105px;height:44px;font-size:5px;padding-left:9px">
      <div class="row"><svg width="6" height="6" viewBox="0 0 10 10"><path d="M2,1 L4,1 L5,3 L4,4 C4.5,5.5 5.5,6.5 7,7 L8,6 L9,7 L9,9 C5,9 1,5 2,1Z" fill="none" stroke="#fff" stroke-width=".8"/></svg>(02) 7341 9256</div>
      <div class="row" style="font-size:4.2px"><svg width="6" height="6" viewBox="0 0 10 10"><rect x="1" y="2.5" width="8" height="5.5" fill="none" stroke="#fff" stroke-width=".8"/><path d="M1,2.5 L5,6 L9,2.5" fill="none" stroke="#fff" stroke-width=".8"/></svg>Enquire@belvorcare.com.au</div>
      <div class="row" style="font-size:4.2px"><svg width="6" height="6" viewBox="0 0 10 10"><circle cx="5" cy="5" r="4" fill="none" stroke="#fff" stroke-width=".8"/><path d="M1,5 H9 M5,1 C2.5,3.5 2.5,6.5 5,9 M5,1 C7.5,3.5 7.5,6.5 5,9" fill="none" stroke="#fff" stroke-width=".6"/></svg>belvorcare.com.au</div>
    </div>
  </section>

  <div class="label" style="left:379px;top:1114px;width:96px;height:21px">Flyer</div>
</div>
</body>
</html>
```